Business card design needed for Automotive Reconditioning business

I have a logo design i just cant decide on the best color or layout for the business card, I will upload all the files so you can see all colors schemes we are considering. I have other file formats if needed let me know.

Target Market(s)

automotive dealerships

Contact Information for Business Card

HERE are the Descriptions and info needed on the card:
Interior Repair: Leather carpet burns panels dash Deoderize
Dealer products and Vin Verify
( spot for name and cell number) My name is Norman Bexley phone 614 352-4180 Title COO www.QuorvalMotive.com

Font styles to use
Sans Serif
Other font styles liked:
• what ever you think looks best

Requirements
Must have
• Must be able to change the name and phone for employees

```html
<!DOCTYPE html>
<html lang="en">
<head>
<meta charset="utf-8">
<title>Quorval Auto Reconditioning Corp. – Business Card</title>
<link rel="stylesheet" href="https://fonts.googleapis.com/css2?family=Roboto:wght@400;500;700&family=Roboto+Condensed:wght@700&display=swap">
<style>
  :root {
    --brand-red: #b71c24;
    --card-white: #ffffff;
    --stage-grey: #e4e4e4;
    --ink-white: #ffffff;
  }
  * { margin: 0; padding: 0; box-sizing: border-box; }
  html, body {
    width: 1200px;
    height: 836px;
    overflow: hidden;
    background: var(--stage-grey);
    font-family: "Roboto", sans-serif;
  }
  .canvas {
    position: relative;
    width: 1200px;
    height: 836px;
  }
  .card {
    position: absolute;
    top: 258px;
    width: 560px;
    height: 320px;
    background: var(--card-white);
    overflow: hidden;
    box-shadow: 0 6px 18px rgba(0, 0, 0, 0.12);
  }
  .card--front { left: 25px; }
  .card--back { left: 615px; }
  .card__shapes {
    position: absolute;
    inset: 0;
    width: 100%;
    height: 100%;
  }
  .brand-name {
    font-family: "Roboto", sans-serif;
    font-weight: 700;
    color: var(--brand-red);
    text-transform: uppercase;
    line-height: 1.1;
  }
  /* front */
  .front__brand {
    position: absolute;
    left: 150px;
    top: 100px;
    width: 300px;
    text-align: center;
    font-size: 30px;
    letter-spacing: 1px;
  }
  .front__web {
    position: absolute;
    left: 110px;
    top: 212px;
    width: 380px;
    text-align: center;
    font-size: 15px;
    letter-spacing: 5px;
    color: var(--brand-red);
    text-transform: uppercase;
  }
  /* back */
  .back__contacts {
    position: absolute;
    left: 38px;
    top: 92px;
    list-style: none;
  }
  .contact {
    display: flex;
    align-items: center;
    gap: 14px;
    margin-bottom: 22px;
    color: var(--ink-white);
    font-size: 15px;
    letter-spacing: 1.5px;
  }
  .contact--phone { font-size: 18px; letter-spacing: 2px; }
  .contact__icon { width: 24px; height: 24px; flex: none; }
  .back__silhouette {
    position: absolute;
    left: 70px;
    top: 215px;
    width: 200px;
    height: 70px;
    border-radius: 40px 60px 8px 8px;
    background: rgba(255, 255, 255, 0.06);
  }
  .back__identity {
    position: absolute;
    left: 392px;
    top: 110px;
    width: 160px;
    text-align: center;
  }
  .back__brand {
    font-size: 17px;
    letter-spacing: 0.5px;
  }
  .back__name {
    margin-top: 14px;
    font-family: "Roboto Condensed", sans-serif;
    font-weight: 700;
    font-size: 20px;
    color: var(--brand-red);
    text-transform: uppercase;
    letter-spacing: 0.5px;
  }
</style>
</head>
<body>
<main class="canvas">

  <section class="card card--front" aria-label="Business card front">
    <svg class="card__shapes" viewBox="0 0 560 320" aria-hidden="true">
      <polygon points="0,120 6,120 66,320 0,320" fill="var(--brand-red)"/>
      <polygon points="0,75 3,75 30,190 22,190" fill="var(--brand-red)"/>
    </svg>
    <div class="front__brand brand-name">Quorval Auto Reconditioning Corp.</div>
    <div class="front__web">www.quorvalmotive.com</div>
  </section>

  <section class="card card--back" aria-label="Business card back">
    <svg class="card__shapes" viewBox="0 0 560 320" aria-hidden="true">
      <polygon points="0,0 292,0 330,320 0,320" fill="var(--brand-red)"/>
      <polygon points="298,0 303,0 352,320 340,320" fill="var(--brand-red)"/>
      <polygon points="309,0 315,0 402,320 374,320" fill="var(--brand-red)"/>
    </svg>

    <div class="back__silhouette" role="img" aria-label="Faint car silhouette decoration"></div>

    <ul class="back__contacts">
      <li class="contact contact--phone">
        <svg class="contact__icon" viewBox="0 0 24 24" aria-hidden="true">
          <circle cx="12" cy="12" r="12" fill="var(--ink-white)"/>
          <path d="M8.6 6.5c.4-.3.9-.2 1.1.2l1.1 2c.2.4.1.8-.2 1.1l-.8.7c.6 1.3 1.6 2.3 2.9 2.9l.7-.8c.3-.3.7-.4 1.1-.2l2 1.1c.4.2.5.7.2 1.1l-1 1.3c-.4.5-1.1.7-1.7.5-3-1-5.3-3.3-6.3-6.3-.2-.6 0-1.3.5-1.7z" fill="var(--brand-red)"/>
        </svg>
        <span>614 352-4180</span>
      </li>
      <li class="contact">
        <svg class="contact__icon" viewBox="0 0 24 24" aria-hidden="true">
          <circle cx="12" cy="12" r="12" fill="var(--ink-white)"/>
          <rect x="6.5" y="8" width="11" height="8" rx="1" fill="var(--brand-red)"/>
          <path d="M6.8 8.4 12 12.4l5.2-4" fill="none" stroke="var(--ink-white)" stroke-width="1"/>
        </svg>
        <span>hello@quorvalmotive.com</span>
      </li>
      <li class="contact">
        <svg class="contact__icon" viewBox="0 0 24 24" aria-hidden="true">
          <circle cx="12" cy="12" r="12" fill="var(--ink-white)"/>
          <rect x="6.5" y="8" width="11" height="8" rx="1" fill="var(--brand-red)"/>
          <path d="M6.8 8.4 12 12.4l5.2-4" fill="none" stroke="var(--ink-white)" stroke-width="1"/>
        </svg>
        <span>www.QuorvalMotive.com</span>
      </li>
    </ul>

    <div class="back__identity">
      <div class="back__brand brand-name">Quorval Auto Reconditioning Corp.</div>
      <div class="back__name">Norman Bexley</div>
    </div>
  </section>

</main>
</body>
</html>
```